Colocation Data Center Web Site

Would be to design a specialized site specifically for a Data Center that provide colocation services to their clients.
This site would need to have a client portal to allow them to see the status of their bills, list of services and to create service tickets.

Industry/Entity Type

It Service

```html
<!DOCTYPE html>
<html lang="en">
<head>
<meta charset="utf-8">
<title>Northvault — Colocation Data Center</title>
<link href="https://fonts.googleapis.com/css2?family=Ubuntu:wght@400;500;700&family=PT+Sans:wght@400;700&display=swap" rel="stylesheet">
<style>
:root{
  --navy:#0b2f63;
  --blue:#1f5a9c;
  --orange:#f7890c;
  --orange-light:#ffa426;
  --text:#4a4a4a;
  --muted:#777;
  --line:#dedede;
  --footer:#141414;
  --white:#fff;
}
*{margin:0;padding:0;box-sizing:border-box}
html,body{width:884px;height:1200px;overflow:hidden;background:var(--white)}
body{position:relative;font-family:"PT Sans",sans-serif;color:var(--text)}
.abs{position:absolute}
.top-strip{left:0;top:0;width:884px;height:5px;background:#e6e6e6}
.brand{left:52px;top:20px;font-family:"Ubuntu",sans-serif;font-weight:500;font-size:36px;color:var(--navy);letter-spacing:-.5px;line-height:1}
.slogan{left:55px;top:66px;font-size:11px;color:var(--blue)}
.search{left:514px;top:51px;width:190px;height:26px;border:1px solid var(--line);font-size:10px;font-style:italic;color:#999;padding:7px 9px}
.search svg{position:absolute;right:7px;top:6px}
.call-label{left:721px;top:41px;font-family:"Ubuntu",sans-serif;font-size:14px;color:var(--blue)}
.call-number{left:720px;top:57px;font-family:"Ubuntu",sans-serif;font-size:20px;font-weight:500;color:var(--navy)}
.main-nav{left:48px;top:92px;width:788px;height:42px;background:linear-gradient(#ffa229,#f7850a);display:flex;border-radius:2px 2px 0 0}
.main-nav a{color:var(--white);text-decoration:none;font-family:"Ubuntu",sans-serif;font-size:14px;display:flex;align-items:center;justify-content:center;border-right:1px solid rgba(255,255,255,.35)}
.main-nav a:last-child{border-right:none}
.slider{left:48px;top:134px;width:788px;height:283px;border:1px solid var(--line);border-top:none;background:var(--white)}
.slide-photo{left:52px;top:137px;width:780px;height:274px;background:linear-gradient(90deg,#cfd3d6 0%,#8e9398 18%,#e9ecee 45%,#f3f5f6 60%,#3a3d42 78%,#2a2c30 100%)}
.caption{left:514px;top:263px;width:318px;height:108px;background:rgba(255,255,255,.93);padding:16px 20px}
.caption .c1{font-family:"Ubuntu",sans-serif;font-size:19px;color:var(--navy)}
.caption .c2{font-family:"Ubuntu",sans-serif;font-weight:500;font-size:23px;color:var(--orange);margin-top:1px}
.caption .c3{font-size:10px;color:var(--muted);margin-top:6px}
.dots-tab{left:398px;top:385px;width:84px;height:28px;background:var(--white);border-radius:40px 40px 0 0}
.dots{left:418px;top:395px;display:flex;gap:4px}
.dots span{width:9px;height:9px;border-radius:50%;background:var(--navy)}
.dots span:first-child{background:var(--orange)}
.feature{top:446px;width:250px}
.feature .thumb{width:238px;height:92px;border:1px solid var(--line);box-shadow:0 1px 2px rgba(0,0,0,.15)}
.feature h3{font-family:"Ubuntu",sans-serif;font-weight:400;font-size:17px;color:var(--blue);margin:8px 0 0 2px}
.feature p{font-size:12px;line-height:17px;color:var(--blue);margin:5px 0 0 2px}
.welcome{left:49px;top:647px;font-family:"Ubuntu",sans-serif;font-size:21px;color:#222}
.welcome b{font-weight:500}
.lead{left:49px;top:680px;font-size:12px;color:#222}
.intro{left:49px;top:706px;width:530px;font-size:10.5px;line-height:18.6px;color:var(--text)}
.login{left:603px;top:644px;width:233px;height:146px;border:1px solid var(--line);border-radius:3px;box-shadow:0 1px 2px rgba(0,0,0,.06)}
.login h4{position:absolute;left:20px;top:12px;font-family:"Ubuntu",sans-serif;font-weight:400;font-size:18px;color:var(--navy)}
.login .field{position:absolute;left:19px;width:191px;height:24px;border:1px solid var(--line);border-radius:3px;font-size:10.5px;color:var(--muted);padding:5px 10px}
.login .forgot{position:absolute;left:23px;top:104px;font-size:8px;color:var(--muted);text-decoration:underline}
.login .btn{position:absolute;left:150px;top:104px;width:61px;height:25px;background:linear-gradient(#123e7a,#06224a);border-radius:3px;color:var(--white);font-size:11px;display:flex;align-items:center;justify-content:center}
.fee-title{left:49px;top:814px;font-family:"Ubuntu",sans-serif;font-size:17px;color:var(--orange)}
.fee-photo{left:48px;top:845px;width:137px;height:167px;border:1px solid var(--line);padding:4px;box-shadow:0 1px 3px rgba(0,0,0,.15);background:var(--white)}
.fee-photo div{width:100%;height:100%;background:linear-gradient(#c8d1d8 0%,#3c4e66 30%,#5b5f66 50%,#dfe2e4 65%,#f0f1f2 100%)}
.fee-text{left:201px;top:843px;width:370px;font-size:10px;line-height:19px}
.fee-text .big{font-size:12px;line-height:19px;color:#333;margin-bottom:6px}
.fee-text p{margin-bottom:7px}
.services{left:603px;top:804px;width:229px;height:247px;border:1px solid var(--line);border-top:none}
.services h4{height:42px;background:linear-gradient(#ffb21c,#f7890c);color:var(--white);font-family:"Ubuntu",sans-serif;font-weight:400;font-size:17.5px;padding:11px 22px}
.services ul{list-style:none;margin:10px 24px 0 25px}
.services li{font-size:10.5px;color:var(--text);height:23px;line-height:21px;border-bottom:1px solid #e8e8e8;padding-left:13px;position:relative}
.services li:last-child{border-bottom:none}
.services li::before{content:"";position:absolute;left:2px;top:7px;border-left:4px solid #888;border-top:4px solid transparent;border-bottom:4px solid transparent}
.footer{left:0;top:1093px;width:884px;height:107px;background:var(--footer)}
.footer-links{left:48px;top:1118px;font-family:"Ubuntu",sans-serif;font-size:11px;color:var(--white)}
.footer-links span{margin:0 4px;color:#aaa}
.copyright{left:49px;top:1144px;font-size:8.5px;color:#ccc}
.social{left:765px;top:1118px;display:flex;gap:4px}
.social span{width:18px;height:18px;border-radius:2px}
</style>
</head>
<body>
<div class="abs top-strip"></div>

<header>
  <div class="abs brand">Northvault</div>
  <div class="abs slogan">Slogan goes here</div>
  <div class="abs search">Search here..
    <svg width="13" height="13" viewBox="0 0 13 13"><circle cx="5.5" cy="5.5" r="4" fill="none" stroke="#888" stroke-width="1.8"/><line x1="8.5" y1="8.5" x2="12" y2="12" stroke="#888" stroke-width="2"/></svg>
  </div>
  <div class="abs call-label">Call Us Now</div>
  <div class="abs call-number">555.210.4470</div>
</header>

<nav class="abs main-nav">
  <a style="width:91px">Home</a>
  <a style="width:95px">About Us</a>
  <a style="width:85px">Services</a>
  <a style="width:88px">Support</a>
  <a style="width:71px">News</a>
  <a style="width:112px">Check Status</a>
  <a style="width:89px">Sitemap</a>
  <a style="width:157px">Contact Us</a>
</nav>

<section>
  <div class="abs slider"></div>
  <div class="abs slide-photo" role="img" aria-label="Data center hall with rows of server racks"></div>
  <div class="abs caption">
    <div class="c1">Vivamus porttitor purus</div>
    <div class="c2">Etiam est nunc venenatis</div>
    <div class="c3">Mauris vel lacus vitae felis vestibulum volutpat Etiam est nunc</div>
  </div>
  <div class="abs dots-tab"></div>
  <div class="abs dots"><span></span><span></span><span></span><span></span></div>
</section>

<section>
  <div class="abs feature" style="left:52px">
    <div class="thumb" role="img" aria-label="Hand using a calculator over billing papers" style="background:linear-gradient(120deg,#eef2f6,#b9c6d4 55%,#dfe6ee)"></div>
    <h3>Check Bill Status</h3>
    <p>Phasellus felis dolor, scelerisque a, tempus eget, lobortis id, libero. Donec scelerisque leo .</p>
  </div>
  <div class="abs feature" style="left:318px">
    <div class="thumb" role="img" aria-label="Team of colleagues looking at a tablet" style="background:linear-gradient(120deg,#6b6f78,#c9a792 50%,#2a2e3a)"></div>
    <h3>Ticket Services</h3>
    <p>Phasellus felis dolor, scelerisque a, tempus eget, lobortis id, libero. Donec scelerisque leo .</p>
  </div>
  <div class="abs feature" style="left:585px">
    <div class="thumb" role="img" aria-label="Couple reviewing payroll at a laptop" style="background:linear-gradient(120deg,#e7e1d6,#c7b28f 50%,#a7a66a)"></div>
    <h3>Payroll Services</h3>
    <p>Phasellus felis dolor, scelerisque a, tempus eget, lobortis id, libero. Donec scelerisque leo .</p>
  </div>
</section>

<main>
  <h1 class="abs welcome" style="font-weight:400">Welcome to <b>Northvault Website Mainpage..</b></h1>
  <div class="abs lead">Nunc tempus felis vitae urna Vivamus porttitor purus nisi eleifend libero, a tempus</div>
  <p class="abs intro">Phasellus felis dolor, scelerisque a, tempus eget, lobortis id, libero. Donec scelerisque leo ac risus. Praesent sit amet est. In dictum, dolor eu dictum porttitor, enim felis viverra mi, eget luctus massa purus quis odio. Etiam nulla massa, pharetra facilisis, volutpat in, imperdiet sit amet, sem. Aliquam nec erat at purus cursus interdum. Vestibulum ligula augue, bibendum accumsan, vestibulum ut, commodo a, mi. Morbi ornare gravida elit. Integer congue</p>

  <h2 class="abs fee-title" style="font-weight:400">Our Fee Structure</h2>
  <div class="abs fee-photo"><div role="img" aria-label="Empty data center floor with raised tiles"></div></div>
  <div class="abs fee-text">
    <p class="big">Mauris vel lacus vitae felis vestibulum volutpat. Etiam est nunc, venenatis in, tristique eu, imperdiet ac, nisl.</p>
    <p>Cum sociis natoque penatibus et magnis dis parturient montes, nascetur ridiculus mus. In iaculis facilisis massa.</p>
    <p>Mauris vel lacus vitae felis vestibulum volutpat. Etiam est nunc, venenatis in, tristique eu, imperdiet ac, nisl. Cum sociis natoque penatibus et magnis dis parturient montes, nascetur ridiculus mus. In iaculis facilisis massa. Etiam eu urna. Sed porta. Suspendisse quam leo, molestie sed, luctus quis, feugiat in, pede. Fusce tellus. Sed metus augue, convallis et, vehicula ut, pulvinar eu, ante.</p>
  </div>
</main>

<aside>
  <div class="abs login">
    <h4>User Login</h4>
    <div class="field" style="top:41px">Username</div>
    <div class="field" style="top:72px">Password</div>
    <div class="forgot">Forgot password?</div>
    <div class="btn">Login</div>
  </div>
  <div class="abs services">
    <h4>Services Provides</h4>
    <ul>
      <li>Phasellus felis dolor</li>
      <li>Scelerisque tempus eget</li>
      <li>Llobortis id libero.</li>
      <li>Donec scelerisque</li>
      <li>Praesent sit amet est</li>
      <li>Dolor eu dictum porttitor</li>
      <li>Enim felis viverra</li>
      <li>Luctus massa purus</li>
    </ul>
  </div>
</aside>

<footer>
  <div class="abs footer"></div>
  <div class="abs footer-links">Home<span>|</span>Data Recovery Process<span>|</span>Data Recovery Services<span>|</span>FAQ<span>|</span>Contact</div>
  <div class="abs copyright">Copyright © 2013 Company Name.&nbsp; All right reserved.&nbsp; Term of Use</div>
  <div class="abs social">
    <span style="background:#3aa6e0"></span>
    <span style="background:#1f74b3"></span>
    <span style="background:#3d61a8"></span>
  </div>
</footer>
</body>
</html>
```